Web App Dashboard Design for a Smart Home

We are a company that gives consultancy and installation services for custom smart home designs to household owners in ON, Canada. For our web application, we are in need of a dashboard design which will display multiple rooms that could be present in a home. This should be a flexible design as the number of rooms where smart devices installed will vary from house to house. We would like to see the name of the rooms and several icons that represent different monitored objects in each room like temperature, light on/off, sound/music on/off, humidity, illuminance, noise level, air quality, for bathrooms and kitchens wet/dry conditions, windows/doors open, curtains open/closed etc. The web application will collect the latest status data from all related sensors and it will be publishing the latest status for each room into this dashboard. Backend of the dashboards should contain nice modern looking houses and it would be good if there are multiple versions of the background pictures that rotate.

Target Market(s)

Mid-Market range house holders who want to increase their comfort and safety with smart home implementations

Industry/Entity Type

Small Business

Number of Pages Required

1 page

Colors
0455a3
3277b5
85acd3
86cae7
fbf289
cadf82
acd037
9bcb3c
faa54b

Requirements
Must have
• - A Flexible Dashboard Design which can hold many rooms but still look sharp even with only 1/2 rooms as well.
• - An smart home icon library that will show the monitored value like temperature, lights on/off, door/window open/close etc.

```html
<!DOCTYPE html>
<html lang="en">
<head>
<meta charset="utf-8">
<title>Smart Home Dashboard</title>
<link rel="stylesheet" href="https://fonts.googleapis.com/css2?family=Roboto:wght@400;500&family=Montserrat:wght@400;500&display=swap">
<style>
  :root {
    --sidebar: #3f7bfc;
    --page: #f8f8f8;
    --card: #ffffff;
    --card-border: #e7e7e7;
    --heading: #0a4fa3;
    --room-title: #1554a8;
    --text: #222222;
    --icon-top: #4d86ff;
    --icon-bottom: #3565e8;
    --alert-top: #ff5a5f;
    --alert-bottom: #e8193a;
    --toggle-off: #dcdcdc;
    --toggle-on: #2fd66f;
    --add-top: #37e47e;
    --add-bottom: #2ccf6d;
  }
  * { box-sizing: border-box; margin: 0; padding: 0; }
  html, body { width: 1200px; height: 886px; overflow: hidden; }
  body { background: var(--page); font-family: 'Roboto', sans-serif; color: var(--text); position: relative; }

  .sidebar { position: absolute; left: 0; top: 0; width: 105px; height: 886px; background: var(--sidebar); color: #fff; }
  .nav-item { position: absolute; left: 0; width: 105px; display: flex; flex-direction: column; align-items: center; font-size: 12px; letter-spacing: .1px; }
  .nav-item svg { width: 30px; height: 30px; fill: #fff; margin-bottom: 2px; }
  .nav-dashboard { top: 34px; }
  .nav-usage { top: 106px; }
  .nav-notifications { top: 178px; }
  .nav-configuration { top: 250px; }
  .nav-logout { top: 799px; }

  .main { position: absolute; left: 207px; top: 0; }
  .page-title { position: absolute; top: 38px; left: 0; font-size: 23px; font-weight: 500; color: var(--heading); white-space: nowrap; }
  .page-subtitle { position: absolute; top: 68px; left: 0; font-size: 12.3px; white-space: nowrap; color: #111; }

  .columns { position: absolute; top: 100px; left: 0; display: flex; gap: 34px; }
  .column { width: 281px; display: flex; flex-direction: column; }
  .room { background: var(--card); border: 1px solid var(--card-border); border-radius: 2px; padding: 17px 18px 0; }
  .room-title { font-size: 13px; color: var(--room-title); margin-bottom: 9px; }
  .device { display: flex; align-items: center; height: 40px; font-family: 'Montserrat', sans-serif; font-size: 12px; }
  .device-icon { width: 32px; height: 32px; border-radius: 3px; background: linear-gradient(var(--icon-top), var(--icon-bottom)); display: flex; align-items: center; justify-content: center; margin-right: 14px; flex: none; }
  .device-icon.alert { background: linear-gradient(var(--alert-top), var(--alert-bottom)); }
  .device-icon svg { width: 20px; height: 20px; fill: #fff; }
  .device-name { flex: 1; }
  .device-value { font-size: 11.5px; margin-right: 4px; }
  .toggle { width: 32px; height: 18px; border-radius: 9px; background: var(--toggle-off); position: relative; }
  .toggle::after { content: ""; position: absolute; top: 2px; left: 2px; width: 14px; height: 14px; border-radius: 50%; background: #fff; }
  .toggle.on { background: var(--toggle-on); }
  .toggle.on::after { left: 16px; }

  .add-room { margin-top: 18px; height: 256px; border-radius: 2px; background: linear-gradient(var(--add-top), var(--add-bottom)); color: #fff; display: flex; flex-direction: column; align-items: center; justify-content: center; font-family: 'Montserrat', sans-serif; font-size: 16px; }
  .add-room svg { width: 24px; height: 24px; margin-bottom: 2px; }
</style>
</head>
<body>
<svg width="0" height="0" style="position:absolute">
  <defs>
    <symbol id="i-bulb" viewBox="0 0 24 24"><path d="M12 2a7 7 0 0 0-4 12.7V17h8v-2.3A7 7 0 0 0 12 2zM9 18.5h6V20H9zM10 21h4v1.5h-4z"/></symbol>
    <symbol id="i-door" viewBox="0 0 24 24"><path d="M3 21V4h3v17zM8 3l10 2v16l-10-1zM14.5 11h1.5v2.5h-1.5zM18.5 7h2.5v14h-2.5z"/></symbol>
    <symbol id="i-bell-off" viewBox="0 0 24 24"><path d="M12 3a6 6 0 0 0-6 6v5l-2 3h16l-2-3V9a6 6 0 0 0-6-6zM10 19h4a2 2 0 0 1-4 0z"/><path d="M3 3l18 18" stroke="#fff" stroke-width="2.4"/><path d="M4.5 2l18 18" stroke="#3d72f2" stroke-width="1.2"/></symbol>
    <symbol id="i-drop" viewBox="0 0 24 24"><path d="M12 2C9 7 6 10.5 6 14.5a6 6 0 0 0 12 0C18 10.5 15 7 12 2z"/><path d="M10 18l4-5" stroke="#3d72f2" stroke-width="1.3"/><circle cx="10" cy="13.5" r="1" fill="#3d72f2"/><circle cx="14" cy="17.5" r="1" fill="#3d72f2"/></symbol>
    <symbol id="i-thermo" viewBox="0 0 24 24"><path d="M6 4a2.5 2.5 0 0 1 5 0v10a4.5 4.5 0 1 1-5 0zM7.7 4v10.8a3 3 0 1 0 1.6 0V4a.8.8 0 0 0-1.6 0z"/><circle cx="8.5" cy="17.8" r="1.8"/><circle cx="17" cy="5" r="2.3" fill="none" stroke="#fff" stroke-width="1.6"/></symbol>
    <symbol id="i-chimney" viewBox="0 0 24 24"><path d="M3 3h18v5H3zM3 9.5h8v4H3zM12.5 9.5H21v4h-8.5zM3 15h4v4H3zM8.5 15h7v4h-7zM17 15h4v4h-4zM3 20.5h18V22H3z"/></symbol>
    <symbol id="i-lamp" viewBox="0 0 24 24"><path d="M8 2h8l3 9H5zM11 12h2v5h-2zM6 18h12v4H6z"/></symbol>
    <symbol id="i-music" viewBox="0 0 24 24"><path d="M9 5l12-3v13.5a3 3 0 1 1-2-2.8V6.5L11 8.4v9.1a3 3 0 1 1-2-2.8z"/></symbol>
    <symbol id="i-alert" viewBox="0 0 24 24"><path d="M10 2h4l-.6 13h-2.8zM10.2 17.5h3.6v3.6h-3.6z"/></symbol>
    <symbol id="i-curtain" viewBox="0 0 24 24"><path d="M2 2h20v2h-1v16h1v2H2v-2h1V4H2zM5 4v16h3.5C7 15 7 9 8.5 4zM19 4h-3.5C17 9 17 15 15.5 20H19zM10.5 4h3v16h-3z"/></symbol>
    <symbol id="i-thumb" viewBox="0 0 24 24"><path d="M2 10h4v11H2zM7.5 10l4-7.5c1.5 0 2.5 1 2.2 2.5L13 9h6.5a2 2 0 0 1 2 2.4l-1.6 8A2 2 0 0 1 18 21H7.5z"/></symbol>
  </defs>
</svg>

<nav class="sidebar">
  <div class="nav-item nav-dashboard">
    <svg viewBox="0 0 24 24"><path d="M12 3l10 9h-3v9h-5v-6h-4v6H5v-9H2z"/></svg>Dashboard
  </div>
  <div class="nav-item nav-usage">
    <svg viewBox="0 0 24 24"><path d="M3 14h3v8H3zM8 11h3v11H8zM13 15h3v7h-3zM18 9h3v13h-3z"/><path d="M3 10l5-5 5 5 7-7" fill="none" stroke="#fff" stroke-width="2"/><circle cx="3" cy="10" r="1.6"/><circle cx="8" cy="5" r="1.6"/><circle cx="13" cy="10" r="1.6"/><circle cx="20" cy="3" r="1.6"/></svg>Usage
  </div>
  <div class="nav-item nav-notifications">
    <svg viewBox="0 0 24 24"><path d="M12 2a1.5 1.5 0 0 1 1.5 1.5v.6A6.5 6.5 0 0 1 18.5 10.5V16l2.5 3H3l2.5-3v-5.5a6.5 6.5 0 0 1 5-6.4v-.6A1.5 1.5 0 0 1 12 2zM9.5 20.5h5a2.5 2.5 0 0 1-5 0z"/></svg>Notifications
  </div>
  <div class="nav-item nav-configuration">
    <svg viewBox="0 0 24 24"><path d="M10 2h4l.6 2.8 2.1 1.2 2.7-.9 2 3.5-2.1 1.9v2.4l2.1 1.9-2 3.5-2.7-.9-2.1 1.2L14 22h-4l-.6-2.8-2.1-1.2-2.7.9-2-3.5 2.1-1.9V11.1L2.6 9.2l2-3.5 2.7.9L9.4 4.8zM12 8.5a3.5 3.5 0 1 0 0 7 3.5 3.5 0 0 0 0-7z"/></svg>Configuration
  </div>
  <div class="nav-item nav-logout">
    <svg viewBox="0 0 24 24"><path d="M10 4H5a2 2 0 0 0-2 2v12a2 2 0 0 0 2 2h5v-3H6V7h4z"/><path d="M14 5l7 7-7 7v-4H9V9h5z"/></svg>Logout
  </div>
</nav>

<main class="main">
  <h1 class="page-title">Dashboard</h1>
  <p class="page-subtitle">Here you can control every aspect of your house, for each room individually</p>

  <div class="columns">
    <div class="column">
      <section class="room" style="height:257px">
        <h2 class="room-title">Main entrance</h2>
        <div class="device"><span class="device-icon"><svg><use href="#i-bulb"/></svg></span><span class="device-name">Porch lamp</span><span class="toggle"></span></div>
        <div class="device"><span class="device-icon"><svg><use href="#i-door"/></svg></span><span class="device-name">Front door</span><span class="toggle on"></span></div>
        <div class="device"><span class="device-icon"><svg><use href="#i-bell-off"/></svg></span><span class="device-name">Alarm</span><span class="toggle"></span></div>
        <div class="device"><span class="device-icon"><svg><use href="#i-drop"/></svg></span><span class="device-name">Humidity</span><span class="device-value">45%</span></div>
        <div class="device"><span class="device-icon"><svg><use href="#i-thermo"/></svg></span><span class="device-name">Temperature</span><span class="device-value">50°F</span></div>
      </section>
      <section class="room" style="height:209px;margin-top:16px">
        <h2 class="room-title">Master bedroom</h2>
        <div class="device"><span class="device-icon"><svg><use href="#i-bulb"/></svg></span><span class="device-name">Ceiling light</span><span class="toggle"></span></div>
        <div class="device"><span class="device-icon"><svg><use href="#i-lamp"/></svg></span><span class="device-name">Left table lamp</span><span class="toggle"></span></div>
        <div class="device"><span class="device-icon"><svg><use href="#i-lamp"/></svg></span><span class="device-name">Right table lamp</span><span class="toggle"></span></div>
        <div class="device"><span class="device-icon"><svg><use href="#i-drop"/></svg></span><span class="device-name">Temperature</span><span class="device-value">73°F</span></div>
      </section>
    </div>

    <div class="column">
      <section class="room" style="height:257px">
        <h2 class="room-title">Living room</h2>
        <div class="device"><span class="device-icon"><svg><use href="#i-bulb"/></svg></span><span class="device-name">Ceiling light</span><span class="toggle on"></span></div>
        <div class="device"><span class="device-icon"><svg><use href="#i-chimney"/></svg></span><span class="device-name">Chimney</span><span class="toggle on"></span></div>
        <div class="device"><span class="device-icon"><svg><use href="#i-lamp"/></svg></span><span class="device-name">Table lamp</span><span class="toggle"></span></div>
        <div class="device"><span class="device-icon"><svg><use href="#i-thermo"/></svg></span><span class="device-name">Temperature</span><span class="device-value">77°F</span></div>
        <div class="device"><span class="device-icon"><svg><use href="#i-music"/></svg></span><span class="device-name">Music</span><span class="toggle"></span></div>
      </section>
      <section class="room" style="height:209px;margin-top:16px">
        <h2 class="room-title">Master bedroom bathroom</h2>
        <div class="device"><span class="device-icon"><svg><use href="#i-bulb"/></svg></span><span class="device-name">Ceiling light</span><span class="toggle"></span></div>
        <div class="device"><span class="device-icon"><svg><use href="#i-thumb"/></svg></span><span class="device-name">Available</span></div>
        <div class="device"><span class="device-icon"><svg><use href="#i-curtain"/></svg></span><span class="device-name">Curtain</span><span class="toggle"></span></div>
        <div class="device"><span class="device-icon"><svg><use href="#i-drop"/></svg></span><span class="device-name">Humidity</span><span class="device-value">78%</span></div>
      </section>
    </div>

    <div class="column">
      <section class="room" style="height:209px">
        <h2 class="room-title">Guest bathroom</h2>
        <div class="device"><span class="device-icon"><svg><use href="#i-bulb"/></svg></span><span class="device-name">Ceiling light</span><span class="toggle"></span></div>
        <div class="device"><span class="device-icon alert"><svg><use href="#i-alert"/></svg></span><span class="device-name">Currently occupied</span></div>
        <div class="device"><span class="device-icon"><svg><use href="#i-curtain"/></svg></span><span class="device-name">Curtain</span><span class="toggle"></span></div>
        <div class="device"><span class="device-icon"><svg><use href="#i-drop"/></svg></span><span class="device-name">Humidity</span><span class="device-value">78%</span></div>
      </section>
      <div class="add-room">
        <svg viewBox="0 0 24 24"><circle cx="12" cy="12" r="12" fill="#fff"/><path d="M10.3 5.5h3.4v4.8h4.8v3.4h-4.8v4.8h-3.4v-4.8H5.5v-3.4h4.8z" fill="#31d774"/></svg>
        Add room
      </div>
    </div>
  </div>
</main>
</body>
</html>
```